New Flyer Design Project for a KBTW Business

I have started an KBTW business and want to create a Flyer and Brochure.
We already have a webpage and logo.
Below link is a reference point
https://www.plimvarto.com.au/design/71834620
webpage is www.belvorcare.com.au
Please match the colour from the webpage and the colour from KBTW webpage.
I also like the tri-folded brochure.
I want pictures associated with the disability sector.
Please use
contact number to be (02) 7341 9256
Email : Enquire@belvorcare.com.au
Thank you.
Disability sector
Disability

```html
<!DOCTYPE html>
<html lang="en">
<head>
<meta charset="utf-8">
<title>Belvor Care – Tri-fold Brochure</title>
<link rel="stylesheet" href="https://fonts.googleapis.com/css2?family=Montserrat:ital,wght@0,600;0,700;0,800;1,700&family=Open+Sans:wght@400;600&display=swap">
<style>
:root{
  --navy:#2e5f72;
  --teal:#3bb39d;
  --mint:#4fd3b4;
  --mint-soft:#dff5ef;
  --paper:#ffffff;
  --page:#edf1f1;
  --ink:#3d4a50;
  --badge:#5b2a86;
}
*{box-sizing:border-box;margin:0;padding:0}
html,body{width:1200px;height:2399px;overflow:hidden}
body{background:var(--page);font-family:"Open Sans",Arial,sans-serif;color:var(--ink);position:relative}
.spread{position:absolute;left:50px;width:1100px;height:850px;display:grid;grid-template-columns:repeat(3,1fr);background:var(--paper);box-shadow:0 10px 30px rgba(30,60,70,.15)}
.spread--outside{top:230px}
.spread--inside{top:1320px}
.panel{position:relative;overflow:hidden;border-right:1px solid rgba(0,0,0,.05)}
.panel:last-child{border-right:none}
.layer{position:absolute;left:0;width:100%}
.photo{position:absolute;left:0;width:100%}
h2{font-family:"Montserrat",Arial,sans-serif;font-weight:800;color:var(--navy);text-transform:uppercase;font-size:19px;line-height:1.1;letter-spacing:.3px}
h3{font-family:"Montserrat",Arial,sans-serif;font-weight:800;color:var(--navy);text-transform:uppercase;font-size:14px;line-height:1.15}
p{font-size:9.5px;line-height:1.5;margin-top:7px}
.copy{position:absolute;left:28px;right:28px}

/* brand word */
.brand{display:flex;align-items:center;gap:8px;font-family:"Montserrat",Arial,sans-serif;font-weight:700;text-transform:uppercase;letter-spacing:1px}
.brand__dot{width:14px;height:14px;border-radius:50%;background:currentColor}

/* values grid */
.values{position:absolute;left:24px;right:24px;top:380px;display:grid;grid-template-columns:repeat(3,1fr);row-gap:18px;text-align:center}
.value__icon{width:38px;height:38px;margin:0 auto;border:2px solid #fff;border-radius:50%;display:flex;align-items:center;justify-content:center}
.value__label{font-size:8.5px;color:#fff;margin-top:5px;line-height:1.25;font-style:italic}

.tagline{position:absolute;right:28px;bottom:30px;width:250px;text-align:right;color:#fff;font-family:"Montserrat",Arial,sans-serif;font-style:italic;font-weight:700;font-size:19px;line-height:1.2}

/* why list */
.reasons{list-style:none;margin-top:14px;border-left:2px solid var(--navy);padding-left:16px}
.reasons li{position:relative;margin-bottom:10px}
.reasons li::before{content:"";position:absolute;left:-26px;top:0;width:18px;height:18px;border-radius:50%;background:var(--teal);border:3px solid #fff;box-shadow:0 0 0 1px var(--teal)}
.reasons strong{font-family:"Montserrat",Arial,sans-serif;font-size:9.5px;font-weight:800;font-style:italic;color:var(--navy);text-transform:uppercase}
.reasons p{margin-top:2px;font-style:italic}

.contact{position:absolute;left:30px;top:690px;color:#fff}
.contact__title{font-family:"Montserrat",Arial,sans-serif;font-weight:600;font-size:20px;margin-bottom:10px}
.contact__row{display:flex;align-items:center;gap:10px;font-size:11px;margin-bottom:8px}
.badge{position:absolute;right:26px;bottom:26px;width:46px;height:46px;border-radius:50%;background:var(--badge)}

/* cover */
.cover__brand{position:absolute;top:80px;left:0;width:100%;justify-content:center;color:#fff;font-size:24px}
.cover__headline{position:absolute;right:26px;top:670px;width:320px;text-align:right;color:#fff;font-family:"Montserrat",Arial,sans-serif;font-weight:800;font-size:25px;line-height:1.1;text-transform:uppercase}
.cover__web{position:absolute;right:26px;bottom:26px;color:#fff;font-size:12px;letter-spacing:1.5px}

/* services */
.ways-head{position:absolute;left:0;top:0;width:100%;height:160px;background:var(--mint);padding:28px 28px 0;color:#fff}
.ways-head h2{color:#fff;text-align:center}
.ways-head p{text-align:center}
.ways{position:absolute;left:24px;right:24px;top:360px}
.way{display:grid;grid-template-columns:44px 1fr;gap:12px;margin-bottom:22px}
.way__icon{width:44px;height:44px;border-radius:50%;border:2px dashed var(--teal);display:flex;align-items:center;justify-content:center}
.services{list-style:none;margin-top:10px}
.services li{font-family:"Montserrat",Arial,sans-serif;font-weight:700;font-style:italic;font-size:9.5px;color:var(--navy);padding-left:14px;position:relative;margin-bottom:4px}
.services li::before{content:"";position:absolute;left:0;top:3px;width:7px;height:7px;background:var(--teal)}
</style>
</head>
<body>

<!-- Outside of the brochure -->
<section class="spread spread--outside">

  <article class="panel panel--mission">
    <div class="copy" style="top:34px">
      <h2>Empowering individuals, one connection at a time</h2>
      <p>The purpose driving Belvor Care is centred on empowering individuals. We see each participant as a unique individual with their own story, aspirations, and potential.</p>
      <p>Our role is to facilitate their journey towards independence and joy. It's not just about the support services we provide; it's about the connections we build, the understanding we foster, and the shared moments of achievement and happiness.</p>
    </div>
    <svg class="layer" style="top:300px;height:550px" viewBox="0 0 367 550" preserveAspectRatio="none" aria-hidden="true">
      <path d="M0 40 Q180 -10 367 30 L367 550 L0 550Z" fill="var(--mint)"/>
    </svg>
    <div class="values">
      <div><div class="value__icon"><svg width="18" height="18" viewBox="0 0 24 24"><path d="M12 21 3 12a5 5 0 0 1 9-6 5 5 0 0 1 9 6z" fill="none" stroke="#fff" stroke-width="2"/></svg></div><div class="value__label">Enhancing Quality of Life</div></div>
      <div><div class="value__icon"><svg width="18" height="18" viewBox="0 0 24 24"><circle cx="12" cy="12" r="9" fill="none" stroke="#fff" stroke-width="2"/><path d="M8 14q4 4 8 0" fill="none" stroke="#fff" stroke-width="2"/></svg></div><div class="value__label">Live Life to the Fullest</div></div>
      <div><div class="value__icon"><svg width="18" height="18" viewBox="0 0 24 24"><path d="M5 12l5 5 9-10" fill="none" stroke="#fff" stroke-width="2.5"/></svg></div><div class="value__label">Trust through Reliability</div></div>
      <div><div class="value__icon"><svg width="18" height="18" viewBox="0 0 24 24"><path d="M12 3l2.6 5.5 6 .7-4.4 4.1 1.2 6-5.4-3-5.4 3 1.2-6L3.4 9.2l6-.7z" fill="none" stroke="#fff" stroke-width="2"/></svg></div><div class="value__label">Commitment to Improving</div></div>
      <div><div class="value__icon"><svg width="18" height="18" viewBox="0 0 24 24"><rect x="5" y="4" width="14" height="16" rx="2" fill="none" stroke="#fff" stroke-width="2"/><path d="M9 10h6M9 14h6" stroke="#fff" stroke-width="2"/></svg></div><div class="value__label">Accountability in All Aspects</div></div>
      <div><div class="value__icon"><svg width="18" height="18" viewBox="0 0 24 24"><path d="M4 20l5-12 7 7z" fill="none" stroke="#fff" stroke-width="2"/><path d="M15 4v3M19 8h-3M18 5l-2 2" stroke="#fff" stroke-width="2"/></svg></div><div class="value__label">Celebrating the Joy of Life</div></div>
    </div>
    <div class="photo" role="img" aria-label="Photo of a smiling woman in a blue top" style="top:560px;height:170px;background:linear-gradient(160deg,#c9aebf,#a98aa5 60%,#8c6f8d)"></div>
    <svg class="layer" style="top:680px;height:170px" viewBox="0 0 367 170" preserveAspectRatio="none" aria-hidden="true">
      <path d="M0 20 Q200 -15 367 30 L367 170 L0 170Z" fill="var(--navy)"/>
      <path d="M0 30 Q200 -5 367 40 L367 170 L0 170Z" fill="var(--mint)"/>
    </svg>
    <div class="tagline">Your dependable KBTW partner on your journey towards independence &amp; a fulfilling life.</div>
  </article>

  <article class="panel panel--why">
    <div class="copy" style="top:34px">
      <h2>Why choose<br>Belvor Care?</h2>
      <p>Belvor Care was born out of a desire to make a real and lasting difference in the lives of our participants and the wider community. We approach each individual with empathy, respect, and a deep commitment to understanding their unique story, needs, and aspirations.</p>
      <ul class="reasons">
        <li><strong>People &amp; family oriented</strong><p>We see each participant as part of our extended family, ensuring a warm, personal touch in everything we do.</p></li>
        <li><strong>Enriching lives</strong><p>Every day, we're fuelled by our mission to make a tangible difference in the community.</p></li>
        <li><strong>Fun &amp; fulfilment</strong><p>We believe in adding a dash of fun to our services because a joyful journey is as important as the destination.</p></li>
      </ul>
    </div>
    <div class="brand" style="position:absolute;top:540px;left:0;width:100%;justify-content:center;color:var(--teal);font-size:20px"><span class="brand__dot"></span>Belvor Care</div>
    <svg class="layer" style="top:620px;height:230px" viewBox="0 0 367 230" preserveAspectRatio="none" aria-hidden="true">
      <path d="M0 10 Q180 60 367 20 L367 230 L0 230Z" fill="var(--navy)"/>
      <path d="M0 22 Q180 72 367 32 L367 230 L0 230Z" fill="var(--mint)"/>
    </svg>
    <div class="contact">
      <div class="contact__title">Contact Info</div>
      <div class="contact__row"><svg width="14" height="14" viewBox="0 0 24 24"><path d="M6 2h4l2 5-3 2a12 12 0 0 0 6 6l2-3 5 2v4a2 2 0 0 1-2 2A18 18 0 0 1 4 4a2 2 0 0 1 2-2z" fill="#fff"/></svg>(02) 7341 9256</div>
      <div class="contact__row"><svg width="14" height="14" viewBox="0 0 24 24"><circle cx="12" cy="12" r="9" fill="none" stroke="#fff" stroke-width="2"/><path d="M3 12h18M12 3c-4 5-4 13 0 18M12 3c4 5 4 13 0 18" fill="none" stroke="#fff" stroke-width="1.5"/></svg>belvorcare.com.au</div>
      <div class="contact__row"><svg width="14" height="14" viewBox="0 0 24 24"><rect x="2" y="5" width="20" height="14" rx="2" fill="#fff"/><path d="M3 6l9 7 9-7" fill="none" stroke="var(--mint)" stroke-width="2"/></svg>Enquire@belvorcare.com.au</div>
    </div>
    <div class="badge" aria-hidden="true"></div>
  </article>

  <article class="panel panel--cover">
    <div class="photo" role="img" aria-label="Photo of a smiling athlete in a wheelchair on a running track" style="top:200px;height:460px;background:linear-gradient(180deg,#b9c7c9 0%,#7f9a7a 30%,#a6534a 55%,#93463f 100%)"></div>
    <svg class="layer" style="top:0;height:300px" viewBox="0 0 367 300" preserveAspectRatio="none" aria-hidden="true">
      <path d="M0 0 H367 V230 Q180 300 0 250Z" fill="var(--mint)"/>
      <path d="M0 0 H367 V215 Q180 280 0 235Z" fill="var(--navy)"/>
    </svg>
    <div class="brand cover__brand"><span class="brand__dot"></span>Belvor Care</div>
    <svg class="layer" style="top:560px;height:290px" viewBox="0 0 367 290" preserveAspectRatio="none" aria-hidden="true">
      <path d="M0 90 Q200 60 367 0 L367 290 L0 290Z" fill="var(--navy)"/>
      <path d="M0 110 Q200 80 367 25 L367 290 L0 290Z" fill="var(--teal)"/>
    </svg>
    <div class="cover__headline">We focus on ability to create a world of possibility.</div>
    <div class="cover__web">www.belvorcare.com.au</div>
  </article>
</section>

<!-- Inside of the brochure -->
<section class="spread spread--inside">

  <article class="panel panel--potential">
    <div class="copy" style="top:34px">
      <h3>Where potential meets possibility</h3>
      <p>At Belvor Care, we're dedicated to helping our participants in New South Wales discover and embrace the fullest version of their lives through our disability support services.</p>
      <p>Our mission is to support our participants in achieving their dreams, overcoming challenges, and embracing every moment with enthusiasm and confidence.</p>
      <p>We're not just a service provider; we're partners in your journey towards empowerment and joy.</p>
      <h3 style="margin-top:22px">Beyond the essentials</h3>
      <p>At Belvor Care, we understand that supporting our participants means going beyond the essentials. It's about enriching your life with activities and experiences that bring joy, excitement, and a sense of accomplishment.</p>
      <p>From leisure activities to skill-building workshops, our lifestyle enhancement programs are designed to add a touch of fun, creativity, and adventure to your daily life, ensuring that every day is an opportunity to experience something new and delightful.</p>
    </div>
    <div class="photo" role="img" aria-label="Photo of a smiling man in a yellow shirt with open hands" style="top:540px;height:220px;background:radial-gradient(ellipse at 50% 60%,#f1d65a 0%,#e9cf6a 30%,#eef3f2 70%)"></div>
    <svg class="layer" style="top:700px;height:150px" viewBox="0 0 367 150" preserveAspectRatio="none" aria-hidden="true">
      <path d="M0 40 Q180 -10 367 30 L367 150 L0 150Z" fill="var(--navy)"/>
      <path d="M0 55 Q180 5 367 45 L367 150 L0 150Z" fill="var(--teal)"/>
    </svg>
  </article>

  <article class="panel panel--ways">
    <div class="ways-head">
      <h2>Ways we deliver care</h2>
      <p>Our services are as diverse as the individuals we support. From providing daily living assistance to fostering personal development and community involvement, we tailor our support to meet the unique needs and aspirations of each participant.</p>
    </div>
    <div class="photo" role="img" aria-label="Photo of a support worker helping a young woman with her studies" style="top:160px;height:180px;background:linear-gradient(135deg,#e8c88f,#c99a5a 45%,#6e6a50)"></div>
    <div class="ways">
      <div class="way">
        <div class="way__icon"><svg width="20" height="20" viewBox="0 0 24 24"><path d="M5 12l5 5 9-10" fill="none" stroke="var(--navy)" stroke-width="2.5"/></svg></div>
        <div><h3>Upskill and gain independence</h3><p>Our tailored approach helps you develop essential life skills, from managing daily tasks to learning new talents. With our supportive guidance, you'll not only gain practical abilities but also a sense of self-reliance and achievement.</p></div>
      </div>
      <div class="way">
        <div class="way__icon"><svg width="20" height="20" viewBox="0 0 24 24"><path d="M3 11l9-7 9 7M5 10v10h14V10" fill="none" stroke="var(--navy)" stroke-width="2"/></svg></div>
        <div><h3>Receive care in your own home</h3><p>Our dedicated team provides personalised support tailored to your needs, ensuring you feel safe, supported, and empowered, all within the comfort of your own living space. It's not just care; it's about enhancing your life at home.</p></div>
      </div>
      <div class="way">
        <div class="way__icon"><svg width="20" height="20" viewBox="0 0 24 24"><circle cx="12" cy="10" r="3" fill="none" stroke="var(--navy)" stroke-width="2"/><path d="M12 21s-7-6-7-11a7 7 0 0 1 14 0c0 5-7 11-7 11z" fill="none" stroke="var(--navy)" stroke-width="2"/></svg></div>
        <div><h3>Get out and about in your community</h3><p>Our services focus on helping you engage with the world around you. From social events to community projects, we support you in building connections, experiencing new activities, and enjoying the richness of community life.</p></div>
      </div>
    </div>
    <svg class="layer" style="top:790px;height:60px" viewBox="0 0 367 60" preserveAspectRatio="none" aria-hidden="true">
      <path d="M0 30 Q180 0 367 25 L367 60 L0 60Z" fill="var(--teal)"/>
    </svg>
  </article>

  <article class="panel panel--support">
    <div class="copy" style="top:34px">
      <h3>Our KBTW support</h3>
      <p>We tailor our comprehensive services to meet your individual needs, fostering independence, community involvement, and an enhanced quality of life under the KBTW framework.</p>
      <h3 style="margin-top:16px">We exist to bring you better care</h3>
      <p>At Belvor Care, we pride ourselves on offering a broad spectrum of services meticulously tailored to meet the unique needs of each participant.</p>
      <p>Our commitment goes beyond basic care; we focus on enriching lives, fostering independence, and ensuring a deep sense of community involvement.</p>
      <p>Whether you're seeking support for daily living, personal development, or community engagement, our dedicated team is here to provide personalised, compassionate, and effective support.</p>
      <p>Discover how our services can be tailored to fit your life, helping you to achieve your goals and live life to its fullest.</p>
      <ul class="services">
        <li>Support Coordination</li>
        <li>Development of Daily Living and Life Skills</li>
        <li>Daily Personal Activities</li>
        <li>Household Tasks</li>
        <li>Community Participation</li>
        <li>Innovative Community Participation</li>
        <li>Assistance with Travel &amp; Transport Arrangements</li>
      </ul>
    </div>
    <div class="photo" role="img" aria-label="Photo of a carer and a woman in a wheelchair reviewing documents at a table" style="top:590px;height:200px;background:linear-gradient(120deg,#f3f4f1,#d9d4c7 40%,#9aa59a 75%,#6f7f74)"></div>
    <svg class="layer" style="top:730px;height:120px" viewBox="0 0 367 120" preserveAspectRatio="none" aria-hidden="true">
      <path d="M0 50 Q180 0 367 30 L367 120 L0 120Z" fill="var(--navy)"/>
      <path d="M0 65 Q180 15 367 45 L367 120 L0 120Z" fill="var(--teal)"/>
    </svg>
  </article>
</section>

</body>
</html>
```